Business Card for Willowcrest Terrain Advisors

We need a business card for Willowcrest Terrain Advisors. The company website address is provided below. The company logo is attached. We provide specialized permafrost services to the mining, transportation, and oil & gas industries. The card should be prepared for:
Dominic Halloway, PhD.
Willowcrest Terrain Advisors
PO Box 418529
Birch Hollow, Alaska 99612
Direct: +1-907-555-2964
Email: dhalloway@terrainadvisors-example.com
Website: www.willowcrestterrainadvisors-example.com

```html
<!DOCTYPE html>
<html lang="en">
<head>
<meta charset="utf-8">
<title>Willowcrest Terrain Advisors – Business Card</title>
<link href="https://fonts.googleapis.com/css2?family=Inter:wght@300;400;600;700&display=swap" rel="stylesheet">
<style>
  :root {
    --stage: #1f1f20;
    --paper: #ffffff;
    --navy: #10161f;
    --ink: #121821;
    --ink-soft: #3a414b;
    --rule: #6b7079;
    --on-navy: #ffffff;
    --on-navy-soft: #c9ced6;
  }
  * { margin: 0; padding: 0; box-sizing: border-box; }
  html, body {
    width: 1200px; height: 780px; overflow: hidden;
    background: var(--stage);
    font-family: "Inter", Arial, sans-serif;
  }
  .stage {
    width: 1200px; height: 780px;
    display: flex; align-items: center; justify-content: center; gap: 48px;
  }
  .card {
    position: relative;
    width: 532px; height: 304px;
    border-radius: 3px;
    box-shadow: 0 14px 30px rgba(0,0,0,0.45);
    overflow: hidden;
  }
  /* Front */
  .card--front { background: var(--paper); color: var(--ink); }
  .front__brand {
    position: absolute; left: 34px; top: 38px;
    font-weight: 700; color: var(--ink); line-height: 1.05;
  }
  .front__brand .brand-main { display: block; font-size: 27px; letter-spacing: 1px; }
  .front__brand .brand-sub { display: block; font-size: 10.5px; letter-spacing: 4.2px; margin-top: 5px; }
  .front__divider { position: absolute; left: 0; top: 0; width: 532px; height: 304px; }
  .front__address {
    position: absolute; left: 34px; bottom: 32px;
    font-size: 12.5px; line-height: 1.5; color: var(--ink);
  }
  .front__person { position: absolute; left: 268px; top: 120px; }
  .person__name { font-size: 26px; line-height: 1.1; color: var(--ink); }
  .person__first { font-weight: 700; }
  .person__last { font-weight: 300; }
  .person__title { font-size: 14px; font-weight: 700; margin-top: 2px; }
  .contact-list { list-style: none; margin-top: 16px; }
  .contact-list li {
    display: flex; align-items: center; gap: 8px;
    font-size: 11.5px; color: var(--ink-soft); margin-bottom: 6px;
  }
  .contact-list svg { width: 12px; height: 12px; flex: none; }
  /* Back */
  .card--back { background: var(--navy); color: var(--on-navy); }
  .back__brand {
    position: absolute; left: 0; right: 0; top: 68px;
    text-align: center; font-weight: 700; color: var(--on-navy); line-height: 1.05;
  }
  .back__brand .brand-main { display: block; font-size: 48px; letter-spacing: 2px; }
  .back__brand .brand-sub { display: block; font-size: 15px; letter-spacing: 8px; margin-top: 8px; }
  .back__services {
    position: absolute; left: 0; right: 0; bottom: 42px; text-align: center;
  }
  .services__heading { font-size: 10px; font-weight: 700; letter-spacing: 0.5px; margin-bottom: 6px; }
  .services__text { font-size: 10.5px; font-weight: 300; color: var(--on-navy-soft); }
</style>
</head>
<body>
<main class="stage">
  <section class="card card--front" aria-label="Card front">
    <div class="front__brand">
      <span class="brand-main">WILLOWCREST</span>
      <span class="brand-sub">TERRAIN ADVISORS</span>
    </div>
    <svg class="front__divider" viewBox="0 0 532 304" aria-hidden="true">
      <line x1="250" y1="92" x2="228" y2="212" stroke="var(--rule)" stroke-width="1"/>
    </svg>
    <div class="front__person">
      <h1 class="person__name"><span class="person__first">Dominic</span> <span class="person__last">Halloway</span></h1>
      <p class="person__title">PhD</p>
      <ul class="contact-list">
        <li>
          <svg viewBox="0 0 24 24" aria-hidden="true"><path fill="var(--ink)" d="M6.6 10.8a15.1 15.1 0 0 0 6.6 6.6l2.2-2.2c.3-.3.7-.4 1-.2 1.1.4 2.3.6 3.6.6.6 0 1 .4 1 1V20c0 .6-.4 1-1 1A17 17 0 0 1 3 4c0-.6.4-1 1-1h3.5c.6 0 1 .4 1 1 0 1.3.2 2.5.6 3.6.1.3 0 .7-.2 1z"/></svg>
          +1-907-555-2964
        </li>
        <li>
          <svg viewBox="0 0 24 24" aria-hidden="true"><rect x="2" y="5" width="20" height="14" rx="2" fill="var(--ink)"/><path d="M3 7l9 6 9-6" fill="none" stroke="#fff" stroke-width="1.6"/></svg>
          dhalloway@terrainadvisors-example.com
        </li>
        <li>
          <svg viewBox="0 0 24 24" aria-hidden="true"><circle cx="12" cy="12" r="10" fill="var(--ink)"/><path d="M2 12h20M12 2c3 3 3 17 0 20M12 2c-3 3-3 17 0 20" fill="none" stroke="#fff" stroke-width="1.3"/></svg>
          www.willowcrestterrainadvisors-example.com
        </li>
      </ul>
    </div>
    <p class="front__address">PO Box 418529<br>Birch Hollow, Alaska 99612</p>
  </section>

  <section class="card card--back" aria-label="Card back">
    <div class="back__brand">
      <span class="brand-main">WILLOWCREST</span>
      <span class="brand-sub">TERRAIN ADVISORS</span>
    </div>
    <div class="back__services">
      <h2 class="services__heading">OUR SERVICES</h2>
      <p class="services__text">We provide specialized permafrost services to the mining, transportation, and oil &amp; gas industries</p>
    </div>
  </section>
</main>
</body>
</html>
```